ultra-minimalist business card

front (black background, matte):

tarik b. hosseny
writer | photographer
get@tarikhosseny.com

back (white background, matte):

a picture speaks a thousand words;
a word draws a thousand pictures.

www.tarikhosseny.com

all text should be small (white or silver - as long as it shows against the black - on the front; black or gray - as long as it shows against the white - on the back).

feel free to get creative in terms of arrangement, alignment, and font type, but remember, the overall style is minimalist, so nothing too fancy, please.

thanks.

```html
<!DOCTYPE html>
<html lang="en">
<head>
<meta charset="utf-8">
<title>tarik b. hosseny — business card</title>
<link rel="stylesheet" href="https://fonts.googleapis.com/css2?family=Arimo:wght@400&display=swap">
<style>
  :root {
    --stage: #26272c;
    --front-bg: #0b0b0c;
    --front-text: #d9d9dc;
    --portrait-tone: #8a8197;
    --back-bg-light: #f1f1f2;
    --back-bg-mid: #dcdcde;
    --back-text: #111113;
  }
  * { box-sizing: border-box; margin: 0; padding: 0; }
  html, body {
    width: 1200px;
    height: 900px;
    overflow: hidden;
    background: var(--stage);
    font-family: "Arimo", Arial, sans-serif;
  }
  .stage {
    width: 1200px;
    height: 900px;
    display: flex;
    flex-direction: column;
    align-items: center;
    justify-content: center;
    gap: 56px;
  }
  .card {
    position: relative;
    width: 660px;
    height: 378px;
    overflow: hidden;
  }
  .card--front { background: var(--front-bg); }
  .portrait {
    position: absolute;
    left: 118px;
    top: 80px;
    width: 200px;
    height: 200px;
    display: block;
  }
  .contact {
    position: absolute;
    left: 392px;
    top: 146px;
    color: var(--front-text);
    font-size: 14px;
    line-height: 1.3;
    letter-spacing: 0.2px;
  }
  .contact__name { font-size: 16px; }
  .card--back { background: var(--back-bg-light); }
  .backdrop {
    position: absolute;
    inset: 0;
    width: 100%;
    height: 100%;
    display: block;
  }
  .motto {
    position: absolute;
    left: 232px;
    top: 170px;
    color: var(--back-text);
    font-size: 15px;
    line-height: 1.3;
    text-align: right;
  }
  .motto__site { margin-top: 30px; }
</style>
</head>
<body>
<main class="stage">
  <section class="card card--front" aria-label="Card front">
    <svg class="portrait" viewBox="0 0 200 200" role="img" aria-label="Circular duotone portrait of the card owner">
      <circle cx="100" cy="100" r="100" fill="var(--portrait-tone)"/>
    </svg>
    <div class="contact">
      <p class="contact__name">tarik b. hosseny</p>
      <p class="contact__role">writer | photographer</p>
      <p class="contact__email">E: get@tarikhosseny.com</p>
    </div>
  </section>

  <section class="card card--back" aria-label="Card back">
    <svg class="backdrop" viewBox="0 0 660 378" preserveAspectRatio="none" role="img" aria-label="Faint grayscale photograph of curved modern architecture">
      <defs>
        <linearGradient id="backdropTone" x1="0" y1="0" x2="1" y2="1">
          <stop offset="0" stop-color="var(--back-bg-light)"/>
          <stop offset="0.55" stop-color="var(--back-bg-mid)"/>
          <stop offset="1" stop-color="var(--back-bg-light)"/>
        </linearGradient>
      </defs>
      <rect width="660" height="378" fill="url(#backdropTone)"/>
    </svg>
    <div class="motto">
      <p>a picture speaks a thousand words.</p>
      <p>a word draws a thousand pictures.</p>
      <p class="motto__site">www.tarikhosseny.com</p>
    </div>
  </section>
</main>
</body>
</html>
```